Real Estate Company Needs a Contemporary/Modern Business Card Design

We need a Contemporary/Modern Business Card Design for a New Real Estate Company based in San Francisco, CA called Colvane Terrish Realtors. We would like to see designs that use the color red for the "Colvane Terrish" and gold for the "Realtors." The design should communicate being Modern and yet Established and Stable.

Industry/Entity Type

Business

```html
<!DOCTYPE html>
<html lang="en">
<head>
<meta charset="utf-8">
<title>Colvane Terrish Realtors – Business Card</title>
<link rel="stylesheet" href="https://fonts.googleapis.com/css2?family=Montserrat:wght@400;500;700&display=swap">
<style>
  :root {
    --backdrop: #e6e6e8;
    --card-white: #ffffff;
    --brand-red: #c3242c;
    --brand-red-dark: #9e1b22;
    --brand-gold: #c9962e;
    --ink: #3a3a3a;
  }
  * { margin: 0; padding: 0; box-sizing: border-box; }
  html, body {
    width: 1200px;
    height: 718px;
    overflow: hidden;
    background: var(--backdrop);
    font-family: "Montserrat", Arial, sans-serif;
  }
  .card {
    position: absolute;
    left: 150px;
    top: 102px;
    width: 900px;
    height: 514px;
    background: var(--card-white);
    box-shadow: 0 14px 40px rgba(0,0,0,0.18);
    overflow: hidden;
  }
  .card-art { position: absolute; inset: 0; }
  .holder {
    position: absolute;
    left: 64px;
    top: 228px;
    color: var(--card-white);
  }
  .holder-name {
    font-weight: 700;
    font-size: 30px;
    letter-spacing: 1px;
    text-transform: uppercase;
  }
  .holder-title {
    margin-top: 6px;
    font-weight: 400;
    font-size: 20px;
  }
  .contacts {
    position: absolute;
    right: 48px;
    top: 50px;
    list-style: none;
    text-align: right;
    color: var(--ink);
    font-size: 15px;
    line-height: 26px;
  }
  .contacts li { display: flex; justify-content: flex-end; align-items: center; gap: 10px; }
  .contact-icon { width: 14px; height: 14px; flex: none; }
  .brand {
    position: absolute;
    left: 380px;
    top: 420px;
    display: flex;
    align-items: center;
    gap: 10px;
  }
  .brand-mark {
    width: 22px;
    height: 22px;
    background: var(--brand-red);
  }
  .brand-name {
    font-weight: 700;
    font-size: 22px;
    color: var(--brand-red);
    letter-spacing: 0.5px;
  }
</style>
</head>
<body>
  <div class="card">
    <svg class="card-art" width="900" height="514" viewBox="0 0 900 514" aria-hidden="true">
      <defs>
        <linearGradient id="redPanel" x1="0" y1="0" x2="1" y2="1">
          <stop offset="0" stop-color="var(--brand-red)"/>
          <stop offset="1" stop-color="var(--brand-red-dark)"/>
        </linearGradient>
      </defs>
      <path d="M0 0 H640 C470 30 360 220 330 514 H0 Z" fill="url(#redPanel)"/>
      <path d="M680 6 C500 40 392 230 362 514" fill="none" stroke="var(--brand-gold)" stroke-width="6"/>
    </svg>

    <div class="holder">
      <p class="holder-name">Rowan Ashby</p>
      <p class="holder-title">Managing Director</p>
    </div>

    <ul class="contacts">
      <li>012 345 6789
        <svg class="contact-icon" viewBox="0 0 14 14"><path d="M3 1 L5 1 L6 4 L4.5 5.5 C5.3 7.2 6.8 8.7 8.5 9.5 L10 8 L13 9 L13 11 C13 12 12 13 11 13 C5.5 13 1 8.5 1 3 C1 2 2 1 3 1 Z" fill="var(--brand-gold)"/></svg>
      </li>
      <li>012 345 6790
        <svg class="contact-icon" viewBox="0 0 14 14"><rect x="3" y="1" width="8" height="12" rx="1.5" fill="var(--brand-gold)"/><rect x="4.5" y="2.5" width="5" height="7" fill="#fff"/></svg>
      </li>
      <li>name@colvaneterrish.com
        <svg class="contact-icon" viewBox="0 0 14 14"><rect x="1" y="3" width="12" height="8" rx="1" fill="var(--brand-gold)"/><path d="M1.5 3.5 L7 8 L12.5 3.5" fill="none" stroke="#fff" stroke-width="1.2"/></svg>
      </li>
      <li>www.colvaneterrish.com
        <svg class="contact-icon" viewBox="0 0 14 14"><circle cx="7" cy="7" r="6" fill="var(--brand-gold)"/><path d="M1 7 H13 M7 1 C4 4 4 10 7 13 M7 1 C10 4 10 10 7 13" fill="none" stroke="#fff" stroke-width="0.9"/></svg>
      </li>
      <li>240 Harbor Lane, San Francisco, CA
        <svg class="contact-icon" viewBox="0 0 14 14"><path d="M7 13 C7 13 2 8 2 5 A5 5 0 0 1 12 5 C12 8 7 13 7 13 Z" fill="var(--brand-gold)"/><circle cx="7" cy="5" r="1.8" fill="#fff"/></svg>
      </li>
    </ul>

    <div class="brand">
      <span class="brand-mark"></span>
      <span class="brand-name">Colvane Terrish Realtors</span>
    </div>
  </div>
</body>
</html>
```